Cleaning service website design

We need a new nice web design(logo will be the same) for a new cleaning service Company:

Informations about Company and logo you can take from flyers in attachments.

This is a cleaning service Company which have simple rules and we would like to show that(in checklist form) on website:

- What we do and that we're Cleaning Green

- Why us?

- How much(our pricing is simple)

Also we would like to communicate with clients by some nice/big pictures on website and the most important thing is our phone number and short/fast Freestimate.

Also there should be some space for description about our Company.

Generally all information on main page can be short: about us, about service(what we do), last reviews, tips (for example: Tip of the week) and other can be some introduction to subpage where will be more information.

There will be few subpages like: About us, About our service, Photos(Before and after), Reviews , Tips, FAQ, Contact, Looking for a Job? - most of them will be just text so you can project just one example.

```html
<!DOCTYPE html>
<html lang="en">
<head>
<meta charset="utf-8">
<title>Tidy Nest House Cleaning</title>
<link href="https://fonts.googleapis.com/css2?family=Ubuntu:wght@400;500&family=Open+Sans:ital,wght@0,400;0,600;1,400&display=swap" rel="stylesheet">
<style>
:root{
  --green:#5fae3e;
  --green-light:#8dc63f;
  --green-deep:#2f7d1d;
  --blue:#1565b7;
  --ink:#333;
  --muted:#555;
  --page:#f2f2f2;
  --panel:#e6e6e6;
  --card:#e9e9e9;
  --footer:#2d2d2d;
  --footer-base:#1f1f1f;
  --white:#fff;
}
*{box-sizing:border-box;margin:0;padding:0}
html,body{width:679px;height:1200px;overflow:hidden}
body{position:relative;background:var(--page);font-family:"Open Sans",Arial,sans-serif;color:var(--ink);font-size:7px;line-height:1.45}
.abs{position:absolute}
ul{list-style:none}

/* header */
.site-header{left:0;top:0;width:679px;height:68px;background:linear-gradient(#fff,#ececec);border-top:3px solid var(--green)}
.brand{left:88px;top:8px;width:96px;height:48px;display:flex;align-items:center;gap:5px}
.brand-dot{width:14px;height:14px;border-radius:50%;background:var(--green)}
.brand-name{font-family:"Ubuntu",sans-serif;font-size:15px;color:var(--green-deep);font-weight:500;line-height:1}
.main-nav{left:252px;top:0;display:flex;height:42px;font-family:"Ubuntu",sans-serif;font-size:6.6px;text-transform:uppercase}
.main-nav a{display:block;padding:0 8px;line-height:42px;color:#333;text-decoration:none}
.main-nav a.is-active{background:var(--green);color:#fff}

/* hero */
.hero{left:0;top:68px;width:679px;height:285px;background:linear-gradient(100deg,#e9efe6 0%,#d8e2d2 35%,#b9c7ad 60%,#6f9b4c 85%,#3f7a2a 100%)}
.hero-floor{left:0;top:190px;width:679px;height:95px;background:linear-gradient(#7fb84d,#4e8f2d)}
.hero-arrow{width:26px;height:26px;border-radius:50%;background:rgba(0,0,0,.7);display:flex;align-items:center;justify-content:center}
.promo{left:362px;top:117px;width:245px;height:114px;background:rgba(255,255,255,.9);text-align:center;font-family:"Ubuntu",sans-serif;padding-top:9px}
.promo-title{font-size:21px;color:#2b2416;line-height:1.1}
.promo-accent{font-size:30px;color:var(--green-deep);letter-spacing:2px;line-height:1.15}
.promo-note{font-size:11px;color:#222;line-height:1.2;margin-top:2px}
.promo-code{font-size:9px;color:#222}
.phone-box{left:431px;top:245px;width:176px;height:36px;background:var(--blue);color:#fff;padding:3px 7px;font-family:"Ubuntu",sans-serif}
.phone-box strong{display:block;font-size:17px;font-weight:400;line-height:1.1}
.phone-box span{font-size:8px}
.call-btn{left:431px;top:285px;width:118px;height:33px;border-radius:3px;background:linear-gradient(#7fd06a,#4fae3b);color:#fff;font-family:"Ubuntu",sans-serif;font-size:17px;text-align:center;line-height:33px}

/* features */
.feature{top:366px;width:170px;text-align:center}
.feature h2{font-family:"Ubuntu",sans-serif;font-weight:400;font-size:11px;color:#444;margin:9px 0 6px}
.checks{text-align:left;display:inline-block;font-size:6.6px;color:#333}
.checks li{position:relative;padding-left:12px;line-height:10.4px}
.checks li::before{content:"";position:absolute;left:1px;top:2px;width:5px;height:3px;border-left:1.3px solid #333;border-bottom:1.3px solid #333;transform:rotate(-45deg)}
.checks li.plain{padding-left:24px}
.checks li.plain::before{display:none}
.read-more{font-style:italic;color:var(--green-light);font-size:6.8px;text-transform:uppercase;letter-spacing:.3px}
.feature .read-more{display:block;margin-top:4px}

/* section bars */
.section-bar{height:31px;background:var(--panel);font-family:"Ubuntu",sans-serif;font-size:12.5px;color:#333;padding-left:12px;line-height:31px}
.section-bar.is-large{font-size:15px}

/* tips */
.tips-intro{left:87px;top:578px;width:116px;font-size:6.8px;line-height:1.5}
.tips-intro .read-more{display:block;margin-top:12px}
.tip-card{top:578px;width:116px;height:140px;background:var(--card);padding:0}
.tip-photo{width:116px;height:115px}
.tip-card p{text-align:center;font-family:"Ubuntu",sans-serif;font-variant:small-caps;font-size:8px;letter-spacing:.5px;line-height:25px;color:#444}

/* about */
.about-menu{left:87px;top:781px;width:76px;font-family:"Ubuntu",sans-serif;font-size:7.5px}
.about-menu li{display:flex;justify-content:space-between;align-items:center;border-bottom:1px solid #ddd;height:21px}
.about-menu li.is-active{color:var(--green)}
.menu-dot{width:8px;height:8px;border-radius:50%;background:#888;position:relative}
.is-active .menu-dot{background:var(--blue)}
.menu-dot::after{content:"";position:absolute;left:2px;top:2.3px;border-left:3.5px solid #fff;border-top:1.7px solid transparent;border-bottom:1.7px solid transparent}
.about-copy{left:172px;top:782px;width:240px;font-size:7px;line-height:1.52}
.about-copy p+p{margin-top:9px}

/* testimonial */
.bar-arrows{right:8px;top:9px;display:flex;gap:1px}
.bar-arrows span{width:12px;height:12px;background:#999;border-radius:2px}
.quote{left:430px;top:784px;width:160px;height:66px;background:var(--panel);padding:6px 8px 0 22px;font-size:6.2px;font-style:italic;color:#555;line-height:1.3}
.quote::before{content:"\201C";position:absolute;left:8px;top:1px;font-size:17px;font-style:normal;color:#666}
.quote::after{content:"";position:absolute;right:24px;bottom:-6px;border-left:6px solid transparent;border-right:6px solid transparent;border-top:6px solid var(--panel)}
.quote-lead{margin-bottom:5px}
.quote-name{left:430px;top:871px;width:114px;text-align:right;font-size:6.6px;font-style:italic;color:var(--blue)}
.avatar{left:555px;top:864px;width:33px;height:24px;border:2px solid #fff;box-shadow:0 0 0 1px #bbb;background:linear-gradient(#5a86b7,#3a5f8f)}

/* promo cards */
.promo-card{top:908px;width:160px;height:190px}
.promo-media{height:99px;border:3px solid #e2e2e2;border-radius:2px}
.estimate-media{background:linear-gradient(135deg,#7ccf6e,#55b449);position:relative;color:#fff;font-family:"Ubuntu",sans-serif}
.estimate-media .line1{position:absolute;left:57px;top:38px;font-size:12px;color:#1d6f9c}
.estimate-media .line2{position:absolute;left:57px;top:55px;font-size:12.5px}
.promo-card h3{font-family:"Ubuntu",sans-serif;font-variant:small-caps;font-weight:400;font-size:10px;color:#333;margin:13px 0 6px;letter-spacing:.2px}
.promo-card p{font-size:6.8px;line-height:1.55}
.promo-card .checks li{padding-left:13px;line-height:10px}
.promo-card .read-more{position:absolute;display:block;left:0;top:176px;width:100%;text-align:center}

/* footer */
.site-footer{left:0;top:1102px;width:679px;height:66px;background:var(--footer);color:#ddd}
.footer-notch{left:329px;top:1102px;border-left:10px solid transparent;border-right:10px solid transparent;border-top:8px solid var(--page)}
.site-footer h4{position:absolute;left:87px;top:17px;font-family:"Ubuntu",sans-serif;font-weight:400;font-size:10.5px;letter-spacing:.3px}
.footer-copy{left:87px;top:33px;width:185px;font-size:6.6px;color:#aaa}
.contact-line{left:289px;display:flex;align-items:center;gap:6px;font-size:5.8px;color:#ddd}
.footer-base{left:0;top:1168px;width:679px;height:32px;background:var(--footer-base);color:#ccc;font-size:6.6px}
.footer-base p{position:absolute;left:87px;top:11px}
.social{right:89px;top:6px;display:flex;gap:6px}
.social span{width:19px;height:19px;border-radius:50%;background:#e4e4e4}
</style>
</head>
<body>

<header class="site-header abs">
  <div class="brand abs"><span class="brand-dot"></span><span class="brand-name">Tidy Nest</span></div>
  <nav class="main-nav abs">
    <a class="is-active" href="#">Home</a><a href="#">About Us</a><a href="#">Services</a><a href="#">Gallery</a><a href="#">Tips</a><a href="#">Looking for a Job</a><a href="#">FAQ</a><a href="#">Reviews</a><a href="#">Contact</a>
  </nav>
</header>

<section class="hero abs" role="img" aria-label="Photo of a bright, spotless bathroom with a round bathtub and green floor"></section>
<div class="hero-floor abs" role="img" aria-label="Green bathroom floor"></div>
<div class="hero-arrow abs" style="left:7px;top:204px"><svg width="10" height="12" viewBox="0 0 10 12"><path d="M7 1 2 6l5 5" fill="none" stroke="#fff" stroke-width="2.2"/></svg></div>
<div class="hero-arrow abs" style="left:642px;top:204px"><svg width="10" height="12" viewBox="0 0 10 12"><path d="m3 1 5 5-5 5" fill="none" stroke="#fff" stroke-width="2.2"/></svg></div>
<div class="promo abs">
  <div class="promo-title">CLEAN &amp; SPARKLING</div>
  <div class="promo-accent">ALWAYS</div>
  <div class="promo-note">*rates are for regular service*</div>
  <div class="promo-code">PROMO:MBCA13</div>
</div>
<div class="phone-box abs"><strong>555-014-2290</strong><span>www.TidyNestHome.ca</span></div>
<div class="call-btn abs">Call Today!</div>

<section class="feature abs" style="left:74px">
  <svg width="46" height="46" viewBox="0 0 46 46"><path d="M12 18h22l-3 24H15z" fill="#555"/><rect x="10" y="14" width="26" height="5" rx="2" fill="#555"/><path d="M16 14c0-8 14-8 14 0" fill="none" stroke="#555" stroke-width="2.5"/></svg>
  <h2>WHAT WE DO</h2>
  <ul class="checks">
    <li>Thoroughly clean your bathrooms,<br>kitchen, bedrooms and living areas</li>
    <li>Mop or vacuum your floors</li>
    <li>Dust surfaces</li>
    <li>Collect garbage</li>
    <li>Make beds</li>
  </ul>
  <span class="read-more">Read more &gt;</span>
</section>

<section class="feature abs" style="left:243px">
  <svg width="46" height="46" viewBox="0 0 46 46"><circle cx="23" cy="23" r="20" fill="none" stroke="#555" stroke-width="3"/><path d="M16.5 18a6.5 6.5 0 1 1 9 6c-2 1-2.5 2.5-2.5 5" fill="none" stroke="#555" stroke-width="3.6"/><circle cx="23" cy="34" r="2.3" fill="#555"/></svg>
  <h2>WHY &nbsp;US</h2>
  <ul class="checks">
    <li>Locally Owned &amp; Operated</li>
    <li>Reliable &amp; Affordable</li>
    <li>All Supplies Provided</li>
    <li>Green Cleaning</li>
    <li>Pet Friendly</li>
    <li>No Contracts</li>
  </ul>
  <span class="read-more">Read more &gt;</span>
</section>

<section class="feature abs" style="left:424px">
  <svg width="46" height="46" viewBox="0 0 46 46"><path d="M17 4h12l-3 7h-6z" fill="#555"/><path d="M19 12h8c10 6 13 16 11 24-1 5-5 7-15 7S9 41 8 36c-2-8 1-18 11-24z" fill="#555"/><text x="23" y="36" text-anchor="middle" font-family="Ubuntu,sans-serif" font-size="17" fill="#fff">$</text></svg>
  <h2>HOW MUCH</h2>
  <ul class="checks">
    <li>$79 for homes less than 1000 sq ft</li>
    <li>$89 for homes 1000-1800 sq ft</li>
    <li>$99 for homes 1800-2600 sq ft</li>
    <li class="plain">*If your home is larger than<br>2600 sq ft please call for a quote.</li>
    <li class="plain">*rates are for regular service*</li>
  </ul>
  <span class="read-more">Read more &gt;</span>
</section>

<div class="section-bar abs" style="left:87px;top:530px;width:505px">TIPS OF THE WEEK</div>
<div class="tips-intro abs">
  <p>We understand that reliability and thoroughness are what you look for in an affordable, professional house cleaning service. We pay attention to your needs. We get the job done!</p>
  <span class="read-more">Read more &gt;</span>
</div>
<article class="tip-card abs" style="left:216px">
  <div class="tip-photo" role="img" aria-label="Photo of someone sweeping a wooden floor" style="background:linear-gradient(#e7dcc2,#c99a5d)"></div>
  <p>Sweeping Solutions</p>
</article>
<article class="tip-card abs" style="left:346px">
  <div class="tip-photo" role="img" aria-label="Photo of a cleaner wiping a kitchen counter" style="background:linear-gradient(#d2a257,#5a6d7a)"></div>
  <p>In The Kitchen</p>
</article>
<article class="tip-card abs" style="left:474px">
  <div class="tip-photo" role="img" aria-label="Photo of a bathtub beside a stone fireplace" style="background:linear-gradient(#4a3a2c,#c9b9a3)"></div>
  <p>Bathroom Boosters</p>
</article>

<div class="section-bar is-large abs" style="left:87px;top:737px;width:332px">ABOUT</div>
<div class="section-bar is-large abs" style="left:430px;top:737px;width:162px">TESTIMONIALS
  <div class="bar-arrows abs"><span></span><span></span></div>
</div>
<ul class="about-menu abs">
  <li class="is-active">About Us <span class="menu-dot"></span></li>
  <li>Mission <span class="menu-dot"></span></li>
  <li>Vision <span class="menu-dot"></span></li>
</ul>
<div class="about-copy abs">
  <p>Have you ever wondered what it would be like if your life was simpler? We're here to help you get there by taking over the chore of house cleaning. With our help you'll have more time to spend on the things that matter most to you.</p>
  <p>With Tidy Nest you not only get a professional service, but you get it at an affordable price. The owner makes it apoint to be at each and every cleaning to assure your needs are met.</p>
</div>
<blockquote class="quote abs">
  <p class="quote-lead">It's about caring, not just cleaning.</p>
  <p>Having personally experienced the struggles of finding quality maid service for our home, we want to make it simpler for families in the Brookfield area.</p>
</blockquote>
<div class="quote-name abs">- Lena &amp; Marcus</div>
<div class="avatar abs" role="img" aria-label="Portrait photo of the reviewers"></div>

<article class="promo-card abs" style="left:87px">
  <div class="promo-media" role="img" aria-label="Photo of four seniors walking on a golf course" style="background:linear-gradient(#dfe9d2,#7f9a63)"></div>
  <h3>Rules</h3>
  <ul class="checks">
    <li>Rule1- Lorem Ipsum is simply dummy</li>
    <li>Rule2- Lorem Ipsum is simply dummy</li>
    <li>Rule3- Lorem Ipsum is simply dummy</li>
  </ul>
  <span class="read-more">Read more &gt;</span>
</article>
<article class="promo-card abs" style="left:258px">
  <div class="promo-media estimate-media">
    <div class="abs" role="img" aria-label="Photo of a smiling cleaner with a vacuum cleaner" style="left:8px;top:6px;width:40px;height:82px;background:linear-gradient(#eaf5e6,#b9dcb0);border-radius:3px"></div>
    <span class="line1">SHORT &amp; FAST</span><span class="line2">FREE ESTIMATE</span>
  </div>
  <h3>Short &amp; Fast Free Estimate</h3>
  <p>Lorem Ipsum is simply dummy text of the printing and typesetting industry. Lorem Ipsum has been the industry's standard</p>
  <span class="read-more">Read more &gt;</span>
</article>
<article class="promo-card abs" style="left:430px">
  <div class="promo-media" role="img" aria-label="Before and after photos of a messy room cleaned up" style="background:linear-gradient(90deg,#8a6f50 0%,#b8967a 48%,#5fae3e 49%,#5fae3e 50%,#e8dfd1 51%,#cdb9a0 100%)"></div>
  <h3>Before &amp; After Reviews</h3>
  <p>Lorem Ipsum is simply dummy text of the printing and typesetting industry. Lorem Ipsum has been the industry's standard</p>
  <span class="read-more">Read more &gt;</span>
</article>

<footer class="site-footer abs">
  <h4>CONTACT INFO</h4>
  <p class="footer-copy abs">Lorem Ipsum is simply dummy text of the printing and typesetting industry.</p>
  <div class="contact-line abs" style="top:37px">
    <svg width="9" height="9" viewBox="0 0 10 10"><rect width="10" height="10" rx="1" fill="#ddd"/><path d="M3 2c-1 2 1 5 4 6l1-1.5-1.5-1-1 .7C4.5 5.6 4 4.8 3.8 4l.8-.8L4 2z" fill="#2d2d2d"/></svg>
    PHONE : 555-014-2290</div>
  <div class="contact-line abs" style="top:51px">
    <svg width="9" height="7" viewBox="0 0 10 8"><rect width="10" height="8" fill="#ddd"/><path d="M0 0l5 4 5-4" fill="none" stroke="#2d2d2d"/></svg>
    EMAIL &nbsp;: www.TidyNestHome.ca</div>
</footer>
<div class="footer-notch abs"></div>
<div class="footer-base abs">
  <p>Copyright © 2013 TidyNestHome All Rights Reserved.</p>
  <div class="social abs"><span></span><span></span><span></span><span></span></div>
</div>

</body>
</html>
```